Double and triple glazing window and door flyer

We are looking for an A4 leaflet which will fold into two advertising our products which are double glazed windows, doors and conservatories. It will have therefore, 4 A5 sides. Our website www.hollowbrookglazeworks.co.uk shows the large range of products we offer.
The heading should read something like "Save money on double or triple glazing NOW". The banner we have for the company is "The best value tmoney can by" Our selling points are: Established since 1988. Family owned and run business which offers exceptional service. 10 year no-risk insured guarantees on all products. We have a range of designs, materials and glazing options for bespoke windows and doors to suit the age and style of your home; all with high security locking.
The latest most advance technology providing outstanding energy savings and sound reduction.
Full Members of the Allied Guild of Pane Fitters (see our website).
Call for a free quote now. Telephone 01632 960418
Text suggestion:
"We are a friendly, family- owned and run company which recognises that trust, integrity and good service are the key foundations for any business.

We offer expert advice, so that you may choose from a very large range of British Made windows, doors and conservatories produced from uPVC, aluminium, hardwood and composite materials: Products individually made from our extensive range to suit your home; whether modern or traditional. All our products are made to the highest standards. Installations are carried out by specialist tradesmen and conform to all Building Regulations."

Target Market(s)

Domestic householders

Font styles to use
Serif

Colors
3176b5
f04a50
33b8a4

Requirements
Must have
• Colourful and eye-catching. Reason to respond.Feel of quality ,reliability and good service
Nice to have
• Made in Britain marque.
• Awarded full membership of PRIME 50 Chartered Casement and Sunroom Fitters Society.
Should not have
• Discounts. Special offers.

```html
<!DOCTYPE html>
<html lang="en">
<head>
<meta charset="utf-8">
<title>Hollowbrook Glazeworks – Glazing Flyer</title>
<link href="https://fonts.googleapis.com/css2?family=Bebas+Neue&family=Montserrat:wght@400;500;600;700;800&display=swap" rel="stylesheet">
<style>
  :root{
    --blue:#3176b5;
    --red:#f04a50;
    --teal:#33b8a4;
    --ink:#1b1b1b;
    --text:#2a2a2a;
    --panel-dark:#1a1a1f;
    --bg:#e9e9e9;
    --white:#ffffff;
  }
  *{box-sizing:border-box;margin:0;padding:0}
  html,body{width:934px;height:1200px;overflow:hidden;background:var(--bg)}
  .stage{position:relative;width:934px;height:1200px}
  .flyer{
    position:absolute;left:42.5px;top:0;width:914px;height:1292px;
    transform:scale(0.9288);transform-origin:0 0;
    background:var(--white);font-family:"Montserrat",sans-serif;color:var(--text);
    overflow:hidden;
  }
  .abs{position:absolute}

  /* header */
  .brand{left:30px;top:70px;width:150px;display:flex;align-items:center;gap:8px}
  .brand-mark{width:14px;height:14px;border-radius:50%;background:var(--ink);flex:none}
  .brand-name{font-weight:700;font-size:17px;color:var(--ink);line-height:1.15}
  .headline{right:32px;top:24px;text-align:right;font-family:"Bebas Neue",sans-serif}
  .headline-main{font-size:94px;line-height:1;color:var(--blue);letter-spacing:1px}
  .headline-sub{font-size:44px;line-height:1;color:var(--ink);margin-top:2px;letter-spacing:.5px}

  /* hero */
  .hero{left:0;top:172px;width:914px;height:395px;
    background:linear-gradient(90deg,#c9707c 0%,#d8aeb8 35%,#b6bfd6 62%,#4b5f8d 100%)}
  .hero-note{left:30px;top:541px;color:var(--white);font-size:14.5px}
  .hero-note b{font-weight:600}
  .slogan{left:415px;top:462px;width:499px;height:105px;background:rgba(20,20,26,.93);padding:8px 0 0 32px}
  .slogan-top{font-weight:800;font-size:44px;line-height:1.05;color:var(--red);letter-spacing:.5px}
  .slogan-bottom{font-weight:400;font-size:38px;line-height:1.05;color:var(--white);letter-spacing:.5px}

  /* intro */
  .intro{left:30px;top:586px;width:480px}
  .intro-kicker{font-size:25px;color:var(--ink);font-weight:400}
  .intro-values{font-size:29px;font-weight:700;margin-top:2px;letter-spacing:-.3px}
  .intro-values .v-blue{color:var(--blue)}
  .intro-values .v-red{color:var(--red)}
  .intro-values .v-teal{color:var(--teal)}
  .intro-rule{width:90px;height:2px;background:var(--ink);margin:10px 0 20px}
  .intro-body{font-size:15px;line-height:1.45;text-align:justify;color:var(--text)}
  .intro-tech{font-size:15px;line-height:1.45;font-weight:600;color:var(--blue);margin-top:14px}

  .gallery{left:30px;top:858px;display:flex;gap:6px}
  .gallery-tile{width:163px;height:162px;border-radius:18px;box-shadow:0 6px 8px rgba(0,0,0,.18)}
  .tile-door{background:linear-gradient(160deg,#b86a4f,#8a3f33 55%,#6b6a55)}
  .tile-bay{background:linear-gradient(170deg,#dfe3e8,#c8715a 60%,#5e7446)}
  .tile-villa{background:linear-gradient(170deg,#b9cfe6,#e8e5df 45%,#b07a5d)}

  /* products */
  .products{left:549px;top:568px;width:337px;height:452px;border-radius:0 0 22px 22px;
    background:linear-gradient(160deg,#3f8ad0 0%,var(--blue) 55%,#2566a6 100%);
    color:var(--white);padding:22px 24px 0 12px}
  .products-title{text-align:center;font-size:26px;font-weight:400;letter-spacing:.3px}
  .products-title b{font-weight:700}
  .products-rule{width:74px;height:2px;background:var(--ink);margin:10px auto 18px}
  .product-list{list-style:none}
  .product-list li{display:flex;align-items:center;gap:14px;height:40.5px;font-size:21px;font-weight:600;
    border-bottom:1px solid rgba(255,255,255,.28)}
  .product-list li:last-child{border-bottom:none}
  .product-list svg{flex:none}

  /* accreditations */
  .accred{left:79px;top:1080px;width:756px;height:100px;border:1.5px solid #cfcfcf;border-radius:16px}
  .accred-title{left:0;top:1066px;width:914px;text-align:center}
  .accred-title span{background:var(--white);padding:0 14px;font-size:21px;font-weight:600;color:var(--blue)}
  .accred-title em{font-style:normal;color:var(--red)}
  .badges{left:100px;top:1105px;width:714px;display:flex;justify-content:space-between;align-items:center}
  .badge{background:#d9dde3;border-radius:4px}
  .badge-a{width:172px;height:28px}
  .badge-b{width:120px;height:50px;background:#cfcfcf}
  .badge-c{width:140px;height:42px;background:#dedede}
  .badge-d{width:46px;height:66px;background:#3c4f91}
  .badge-e{width:106px;height:54px;background:#e05c4a}

  /* contact */
  .call{left:0;top:1215px;width:412px;height:62px;border-radius:0 31px 31px 0;
    background:linear-gradient(90deg,#d6353b,var(--red) 70%,#f36a6f);color:var(--white)}
  .call svg{position:absolute;left:38px;top:6px}
  .call-label{position:absolute;left:88px;top:3px;font-size:16px;font-weight:500}
  .call-number{position:absolute;left:85px;top:19px;font-size:38px;font-weight:800;letter-spacing:.5px}
  .contact{left:440px;top:1219px;font-size:19.5px;font-weight:500;color:var(--ink)}
  .contact-row{display:flex;align-items:center;gap:12px;height:29px}
</style>
</head>
<body>
<div class="stage">
  <article class="flyer">
    <div class="abs brand">
      <span class="brand-mark"></span>
      <span class="brand-name">Hollowbrook Glazeworks</span>
    </div>
    <header class="abs headline">
      <div class="headline-main">SAVE MONEY ON</div>
      <div class="headline-sub">DOUBLE OR TRIPLE GLAZING NOW</div>
    </header>

    <div class="abs hero" role="img" aria-label="White uPVC conservatory with glass roof attached to a brick house, tinted red to blue"></div>
    <p class="abs hero-note">Our selling points are:&nbsp; <b>Established since 1988</b></p>
    <div class="abs slogan">
      <div class="slogan-top">THE BUY VALUE</div>
      <div class="slogan-bottom">THAT MONEY CAN BY</div>
    </div>

    <section class="abs intro">
      <h2 class="intro-kicker">We're Committed To</h2>
      <div class="intro-values"><span class="v-blue">Excellence,</span> <span class="v-red">Integrity</span> <span class="v-red">&amp;</span> <span class="v-teal">Service</span></div>
      <div class="intro-rule"></div>
      <p class="intro-body">Family owned and run business which offers exceptional service. 10 year no-risk insured guarantees on all products. We have a range of designs, materials and glazing options for bespoke windows and doors to suit the age and style of your home; all with high security locking.</p>
      <p class="intro-tech">The latest most advance technology providing outstanding energy savings and sound reduction.</p>
    </section>

    <div class="abs gallery">
      <div class="gallery-tile tile-door" role="img" aria-label="Red composite front door in a brick porch"></div>
      <div class="gallery-tile tile-bay" role="img" aria-label="House with white bay windows and red tiled bay roof"></div>
      <div class="gallery-tile tile-villa" role="img" aria-label="Tall white period house with sash windows and a balcony"></div>
    </div>

    <section class="abs products">
      <h2 class="products-title">OUR <b>PRODUCTS</b></h2>
      <div class="products-rule"></div>
      <ul class="product-list">
        <li><svg width="20" height="20" viewBox="0 0 20 20"><circle cx="10" cy="10" r="10" fill="#fff"/><path d="M8 5.5l4.5 4.5L8 14.5" stroke="#3176b5" stroke-width="2.4" fill="none"/></svg>uPVC Windows</li>
        <li><svg width="20" height="20" viewBox="0 0 20 20"><circle cx="10" cy="10" r="10" fill="#fff"/><path d="M8 5.5l4.5 4.5L8 14.5" stroke="#3176b5" stroke-width="2.4" fill="none"/></svg>Hardwood Windows</li>
        <li><svg width="20" height="20" viewBox="0 0 20 20"><circle cx="10" cy="10" r="10" fill="#fff"/><path d="M8 5.5l4.5 4.5L8 14.5" stroke="#3176b5" stroke-width="2.4" fill="none"/></svg>Composite Doors</li>
        <li><svg width="20" height="20" viewBox="0 0 20 20"><circle cx="10" cy="10" r="10" fill="#fff"/><path d="M8 5.5l4.5 4.5L8 14.5" stroke="#3176b5" stroke-width="2.4" fill="none"/></svg>uPVC Doors</li>
        <li><svg width="20" height="20" viewBox="0 0 20 20"><circle cx="10" cy="10" r="10" fill="#fff"/><path d="M8 5.5l4.5 4.5L8 14.5" stroke="#3176b5" stroke-width="2.4" fill="none"/></svg>Hardwood Doors</li>
        <li><svg width="20" height="20" viewBox="0 0 20 20"><circle cx="10" cy="10" r="10" fill="#fff"/><path d="M8 5.5l4.5 4.5L8 14.5" stroke="#3176b5" stroke-width="2.4" fill="none"/></svg>Folding &amp; Sliding Doors</li>
        <li><svg width="20" height="20" viewBox="0 0 20 20"><circle cx="10" cy="10" r="10" fill="#fff"/><path d="M8 5.5l4.5 4.5L8 14.5" stroke="#3176b5" stroke-width="2.4" fill="none"/></svg>Conservatories</li>
        <li><svg width="20" height="20" viewBox="0 0 20 20"><circle cx="10" cy="10" r="10" fill="#fff"/><path d="M8 5.5l4.5 4.5L8 14.5" stroke="#3176b5" stroke-width="2.4" fill="none"/></svg>Juliet Balconies</li>
        <li><svg width="20" height="20" viewBox="0 0 20 20"><circle cx="10" cy="10" r="10" fill="#fff"/><path d="M8 5.5l4.5 4.5L8 14.5" stroke="#3176b5" stroke-width="2.4" fill="none"/></svg>More...</li>
      </ul>
    </section>

    <div class="abs accred"></div>
    <h2 class="abs accred-title"><span>OUR <em>ACCREDITATIONS</em></span></h2>
    <div class="abs badges">
      <div class="badge badge-a" role="img" aria-label="Trade review listing badge"></div>
      <div class="badge badge-b" role="img" aria-label="Registered installer badge"></div>
      <div class="badge badge-c" role="img" aria-label="Allied Guild of Pane Fitters membership badge"></div>
      <div class="badge badge-d" role="img" aria-label="PRIME 50 Chartered Casement and Sunroom Fitters Society badge"></div>
      <div class="badge badge-e" role="img" aria-label="Government endorsed standards badge"></div>
    </div>

    <div class="abs call">
      <svg width="30" height="50" viewBox="0 0 30 50"><rect x="2" y="2" width="26" height="46" rx="5" fill="none" stroke="#fff" stroke-width="3.5"/><line x1="2" y1="38" x2="28" y2="38" stroke="#fff" stroke-width="3"/><circle cx="15" cy="43" r="2" fill="#fff"/></svg>
      <span class="call-label">Call for a free quote now</span>
      <span class="call-number">01632 960418</span>
    </div>
    <div class="abs contact">
      <div class="contact-row"><svg width="20" height="14" viewBox="0 0 20 14"><rect width="20" height="14" rx="1" fill="#f04a50"/><path d="M1 1l9 7 9-7" stroke="#fff" stroke-width="1.5" fill="none"/></svg>hello@hollowbrookglazeworks.co.uk</div>
      <div class="contact-row"><svg width="20" height="20" viewBox="0 0 20 20" fill="none" stroke="#f04a50" stroke-width="1.5"><circle cx="10" cy="10" r="8.5"/><ellipse cx="10" cy="10" rx="4" ry="8.5"/><line x1="1.5" y1="10" x2="18.5" y2="10"/><line x1="3" y1="5.5" x2="17" y2="5.5"/><line x1="3" y1="14.5" x2="17" y2="14.5"/></svg>www.hollowbrookglazeworks.co.uk</div>
    </div>
  </article>
</div>
</body>
</html>
```